Magazine advertisement

I need a company advertisement for magazine prints. I need to be able to scale it to different sizes if need be. I need it to showcase our brand, VornaDrive have our phone number 582.463.9047 our contact email address sales@vornadrive.net and web address www.vornadrive.net

Target Market(s)

automotive / tractor pulling

Industry/Entity Type

automotive / racing

Colors
EB3D1F
EC4F4E
F09395
F8D3D4
FCEDEE

Requirements
Must have
• our logo, our color scheme (pantone red 1795, white, black, silver

```html
<!DOCTYPE html>
<html lang="en">
<head>
<meta charset="utf-8">
<title>VornaDrive – Print Collateral</title>
<link href="https://fonts.googleapis.com/css2?family=Oswald:wght@400;500;700&family=Roboto:wght@400;500&display=swap" rel="stylesheet">
<style>
  :root {
    --red: #d7262e;
    --red-dark: #b81d24;
    --white: #ffffff;
    --black: #111111;
    --ink: #222222;
    --silver-light: #e4e4e4;
    --silver: #b9b9b9;
    --silver-dark: #8a8a8a;
    --grid: #e6e6e6;
    --shadow: 0 2px 6px rgba(0,0,0,0.28);
  }
  * { margin: 0; padding: 0; box-sizing: border-box; }
  html, body { width: 927px; height: 1200px; overflow: hidden; background: var(--white); }
  body { position: relative; font-family: "Roboto", Arial, sans-serif; color: var(--ink); }

  .piece { position: absolute; box-shadow: var(--shadow); overflow: hidden; }

  .brand-name {
    font-family: "Oswald", Arial, sans-serif;
    font-weight: 700;
    text-transform: uppercase;
    letter-spacing: 2px;
    line-height: 1;
    white-space: nowrap;
  }
  .phone {
    font-family: "Oswald", Arial, sans-serif;
    font-weight: 700;
    line-height: 1;
    white-space: nowrap;
  }
  .contact-line { font-family: "Oswald", Arial, sans-serif; font-weight: 500; line-height: 1.25; white-space: nowrap; }

  /* Flyer */
  .flyer { left: 61px; top: 61px; width: 400px; height: 553px; background: var(--white); }
  .flyer__grid {
    position: absolute; left: 26px; top: 70px; width: 348px; height: 440px;
    background-image:
      linear-gradient(var(--grid) 1px, transparent 1px),
      linear-gradient(90deg, var(--grid) 1px, transparent 1px);
    background-size: 24px 24px;
  }
  .flyer__brand { position: absolute; left: 0; right: 0; top: 78px; text-align: center; font-size: 34px; color: var(--red); }
  .flyer__art {
    position: absolute; left: 52px; top: 124px; width: 300px; height: 200px;
    background: radial-gradient(ellipse at 45% 55%, #f4f4f4 0%, #d4d4d4 70%, #c4c4c4 100%);
    border-radius: 46% 40% 36% 44%;
  }
  .flyer__headline {
    position: absolute; left: 0; right: 0; top: 330px; text-align: center;
    font-family: "Oswald", Arial, sans-serif; font-weight: 700; font-size: 21px; color: var(--red);
  }
  .flyer__body {
    position: absolute; left: 44px; right: 44px; top: 360px; text-align: center;
    font-size: 10px; line-height: 1.4; color: var(--black);
  }
  .flyer__phone { position: absolute; left: 140px; top: 515px; font-size: 21px; color: var(--black); }
  .flyer__links { position: absolute; left: 265px; top: 514px; font-size: 9.5px; color: var(--black); }

  /* Business card */
  .card { left: 474px; top: 336px; width: 391px; height: 278px; background: radial-gradient(ellipse at 50% 40%, #e0343b 0%, var(--red) 55%, var(--red-dark) 100%); color: var(--white); }
  .card__art {
    position: absolute; left: 118px; top: 28px; width: 152px; height: 150px;
    background: radial-gradient(circle at 40% 45%, var(--silver-light) 0%, var(--silver) 60%, var(--silver-dark) 100%);
    border-radius: 48% 42% 40% 46%;
  }
  .card__brand { position: absolute; left: 0; right: 0; top: 94px; text-align: center; font-size: 38px; color: var(--black); }
  .card__tagline {
    position: absolute; left: 0; right: 0; top: 207px; text-align: center;
    font-size: 8px; letter-spacing: 3px; text-transform: uppercase;
  }
  .card__phone { position: absolute; left: 0; right: 0; top: 222px; text-align: center; font-size: 20px; }
  .card__email { position: absolute; left: 22px; top: 252px; font-size: 10px; }
  .card__web { position: absolute; right: 22px; top: 252px; font-size: 10px; }

  /* Folded brochure */
  .brochure { left: 61px; top: 636px; width: 804px; height: 493px; background: var(--white); }
  .brochure__back {
    position: absolute; left: 0; top: 0; width: 402px; height: 100%;
    background: var(--red); color: var(--white); text-align: center;
  }
  .brochure__phone { position: absolute; left: 0; right: 0; top: 264px; font-size: 20px; }
  .brochure__links { position: absolute; left: 0; right: 0; top: 302px; font-size: 11px; line-height: 2.4; }
  .brochure__cover { position: absolute; left: 402px; top: 0; width: 402px; height: 100%; text-align: center; }
  .brochure__brand { position: absolute; left: 0; right: 0; top: 240px; font-size: 44px; color: var(--red); }
  .brochure__title {
    position: absolute; left: 0; right: 0; top: 348px;
    font-family: "Oswald", Arial, sans-serif; font-weight: 700; font-size: 14px; line-height: 1.3;
    text-transform: uppercase; color: var(--black);
  }
  .brochure__subtitle { position: absolute; left: 0; right: 0; top: 386px; font-family: "Oswald", Arial, sans-serif; font-size: 10px; color: var(--black); }
</style>
</head>
<body>

  <section class="piece flyer">
    <div class="flyer__grid"></div>
    <div class="brand-name flyer__brand">VornaDrive</div>
    <div class="flyer__art" role="img" aria-label="Pencil-style drawing of a turbocharger"></div>
    <h2 class="flyer__headline">BUILT TO WIN</h2>
    <p class="flyer__body">We’ll help you perform like a winner, from truck and tractor pulling to drag racing. Our turbochargers are equipped with the capacity to power everything from high-end sports cars to snowmobiles.</p>
    <div class="phone flyer__phone">582.463.9047</div>
    <div class="contact-line flyer__links">sales@vornadrive.net<br>www.vornadrive.net</div>
  </section>

  <section class="piece card">
    <div class="card__art" role="img" aria-label="Silver rendering of a turbocharger housing"></div>
    <div class="brand-name card__brand">VornaDrive</div>
    <div class="card__tagline">Custom Turbochargers</div>
    <div class="phone card__phone">582.463.9047</div>
    <div class="contact-line card__email">sales@vornadrive.net</div>
    <div class="contact-line card__web">www.vornadrive.net</div>
  </section>

  <section class="piece brochure">
    <div class="brochure__back">
      <div class="phone brochure__phone">582.463.9047</div>
      <div class="contact-line brochure__links">sales@vornadrive.net<br>www.vornadrive.net</div>
    </div>
    <div class="brochure__cover">
      <div class="brand-name brochure__brand">VornaDrive</div>
      <h2 class="brochure__title">Custom<br>Turbochargers</h2>
      <div class="brochure__subtitle">for Extreme Motorsports</div>
    </div>
  </section>

</body>
</html>
```